全国の1人〜2人で営業されている理・美容室のオーナーさん方にコロナでも全く影響を受けてない当サロンのノウハウを読んで頂きたいと思っています。
これからのサロンのあり方、考え方、今すぐに取り入れるべき技術や商品、売り上げの上げ方などをお伝えします。本気で環境を変えたい方、美容師の仕事、接客、人をキレイにすることが大好きな方、意識の高いお客様に囲まれずっと通って頂けるような、そんな美容室を一緒に作って行きたいです。

この度はご提案、修正と本当にありがとうございました。最後の最後までかなり悩みました。
初めての電子書籍で良い表紙デザインと出会うことが出来ました。

今回、ご提案頂いた皆さん、本当にありがとうございました。初心者の自分に親身になって頂き、皆さんの丁寧なデザインに感動しました。また2冊目も考えています。ご縁があればまたよろしくお願いします。

```html
<!DOCTYPE html>
<html lang="ja">
<head>
<meta charset="utf-8">
<title>これからのサロンが生き残る方法</title>
<link href="https://fonts.googleapis.com/css2?family=M+PLUS+1p:wght@500;700;800&display=swap" rel="stylesheet">
<style>
  :root {
    --pink: #f0707f;
    --ink: #1d1d1d;
    --paper: #ffffff;
    --sky: #cfe4f7;
    --figure-red: #e9536a;
    --figure-blue: #7fb3e0;
  }
  * { margin: 0; padding: 0; box-sizing: border-box; }
  html, body { width: 751px; height: 1200px; overflow: hidden; background: var(--paper); }
  body { font-family: "M PLUS 1p", sans-serif; color: var(--ink); }
  .cover { position: relative; width: 751px; height: 1200px; background: var(--paper); overflow: hidden; }

  .title-band { position: absolute; left: 0; background: var(--pink); color: var(--paper); font-weight: 800; line-height: 1; white-space: nowrap; }
  .title-lead { top: 18px; width: 728px; height: 58px; padding-left: 10px; font-size: 43px; display: flex; align-items: center; }
  .title-plain { position: absolute; left: 8px; top: 102px; font-size: 58px; font-weight: 800; line-height: 1; }
  .title-salon { top: 196px; width: 228px; height: 78px; font-size: 66px; display: flex; align-items: center; padding-left: 10px; }
  .title-particle { position: absolute; left: 240px; top: 220px; font-size: 44px; font-weight: 800; color: var(--pink); line-height: 1; }
  .title-end { top: 290px; width: 385px; height: 76px; font-size: 58px; display: flex; align-items: center; padding-left: 8px; }

  .illustration { position: absolute; left: 380px; top: 372px; width: 300px; height: 370px; }

  .author { position: absolute; right: 12px; top: 745px; background: var(--pink); color: var(--paper); font-size: 20px; font-weight: 700; padding: 6px 18px; letter-spacing: 1px; }

  .blurb { position: absolute; left: 0; top: 795px; width: 751px; height: 405px; background: var(--sky); }

  .question { position: absolute; right: 20px; top: 30px; height: 360px; writing-mode: vertical-rl; font-size: 34px; font-weight: 800; line-height: 1.55; }
  .question .accent { color: var(--pink); font-size: 48px; }
  .question .accent-mid { color: var(--pink); font-size: 42px; }

  .summary { position: absolute; left: 372px; top: 30px; height: 330px; writing-mode: vertical-rl; font-size: 19px; font-weight: 700; line-height: 1.5; }

  .audience-head { position: absolute; left: 292px; top: 30px; width: 46px; height: 330px; background: var(--paper); writing-mode: vertical-rl; font-size: 22px; font-weight: 800; display: flex; align-items: center; padding-top: 10px; }

  .audience-list { position: absolute; left: 30px; top: 30px; height: 340px; writing-mode: vertical-rl; list-style: none; font-size: 22px; font-weight: 700; }
  .audience-list li { margin-left: 30px; display: flex; align-items: center; }
  .audience-list li::before { content: ""; width: 18px; height: 18px; background: var(--paper); margin-bottom: 10px; }
</style>
</head>
<body>
<main class="cover">
  <h1>
    <span class="title-band title-lead">コロナや景気に左右されない</span>
    <span class="title-plain">これからの</span>
    <span class="title-band title-salon">サロン</span>
    <span class="title-particle">が</span>
    <span class="title-band title-end">生き残る方法</span>
  </h1>

  <svg class="illustration" role="img" aria-label="大きなはさみを抱えた美容師のイラスト" viewBox="0 0 300 370">
    <rect x="0" y="0" width="300" height="370" rx="20" fill="var(--figure-blue)" opacity="0.35"/>
    <rect x="40" y="60" width="220" height="250" rx="40" fill="var(--figure-red)" opacity="0.35"/>
  </svg>

  <p class="author">著者：たかはし　みなと</p>

  <section class="blurb">
    <p class="question"><span class="accent">100人</span>の心を<br>満たす前にまず<span class="accent-mid">1人</span>の<br><span class="accent-mid">お客様</span>を満足させて<br>いますか？</p>
    <p class="summary">これからを生き抜くサロンの<br>あり方、考え方、今すぐに<br>取り入れるべき技術や商品、<br>売り上げの上げ方を教えます。</p>
    <p class="audience-head">当てはまる人必見！</p>
    <ul class="audience-list">
      <li>美容室経営者</li>
      <li>独自性が欲しいサロン</li>
      <li>独立を考えている美容師</li>
    </ul>
  </section>
</main>
</body>
</html>
```